Dyrano In-home Personal Training

I would like to have some eye-catching business card design. Opened to any ideas.

The business idea: mobile fitness - train clients at their places

Target Market(s)

General population, 20-60 years old

Industry/Entity Type

Fitness

Contact Information for Business Card

The information to include:
Name: Marta
Call or text: 306-555-0187
Website: Dyrano.ca
Please use the attached logo

Requirements
Should not have
• No orange or purple colours please

```html
<!DOCTYPE html>
<html lang="en">
<head>
<meta charset="utf-8">
<title>Dyrano In-home Personal Training — Business Card</title>
<link href="https://fonts.googleapis.com/css2?family=Lato:wght@300;400;700&display=swap" rel="stylesheet">
<style>
  :root {
    --backdrop: #3b322d;
    --card: #1c1c1d;
    --ink: #ffffff;
    --ink-soft: #e6e6e6;
    --rule: #d9d9d9;
  }
  * { box-sizing: border-box; margin: 0; padding: 0; }
  html, body {
    width: 1200px;
    height: 847px;
    overflow: hidden;
    background: var(--backdrop);
    font-family: "Lato", sans-serif;
    color: var(--ink);
  }
  .sheet {
    width: 1200px;
    height: 847px;
    display: flex;
    align-items: center;
    justify-content: center;
    gap: 40px;
  }
  .card {
    width: 540px;
    height: 309px;
    background: var(--card);
    border-radius: 3px;
    box-shadow: 0 10px 30px rgba(0,0,0,0.45);
    position: relative;
    overflow: hidden;
  }

  /* wordmark */
  .brand {
    display: flex;
    flex-direction: column;
    align-items: flex-start;
  }
  .brand-row {
    display: flex;
    align-items: center;
    gap: 12px;
  }
  .brand-dot {
    border: 2px solid var(--ink);
    border-radius: 50%;
  }
  .brand-name {
    font-weight: 300;
    letter-spacing: 0.14em;
    line-height: 1;
    color: var(--ink);
  }
  .brand-tagline {
    font-weight: 400;
    text-transform: uppercase;
    letter-spacing: 0.32em;
    color: var(--ink-soft);
  }

  /* front */
  .card-front .brand {
    position: absolute;
    left: 70px;
    top: 108px;
  }
  .card-front .brand-dot { width: 44px; height: 44px; }
  .card-front .brand-name { font-size: 56px; }
  .card-front .brand-tagline {
    font-size: 10px;
    margin: 8px 0 0 58px;
  }

  /* back */
  .card-back .brand {
    position: absolute;
    left: 40px;
    top: 118px;
  }
  .card-back .brand-row { gap: 9px; }
  .card-back .brand-dot { width: 30px; height: 30px; }
  .card-back .brand-name { font-size: 36px; }
  .card-back .brand-tagline {
    font-size: 7px;
    letter-spacing: 0.28em;
    margin: 6px 0 0 40px;
  }
  .divider {
    position: absolute;
    left: 290px;
    top: 80px;
    width: 1.5px;
    height: 150px;
    background: var(--rule);
  }
  .contact {
    position: absolute;
    left: 318px;
    top: 82px;
  }
  .person-name {
    font-weight: 700;
    font-size: 22px;
    line-height: 1.1;
  }
  .person-role {
    font-weight: 400;
    font-size: 15px;
    color: var(--ink-soft);
    margin-top: 2px;
  }
  .contact-list {
    list-style: none;
    margin-top: 20px;
  }
  .contact-list li {
    display: flex;
    align-items: center;
    gap: 10px;
    font-size: 15px;
    line-height: 1.35;
  }
  .contact-list svg {
    width: 14px;
    height: 14px;
    flex: none;
    fill: none;
    stroke: var(--ink);
    stroke-width: 1.6;
  }
</style>
</head>
<body>
<main class="sheet">
  <section class="card card-front">
    <div class="brand">
      <div class="brand-row">
        <span class="brand-dot"></span>
        <span class="brand-name">Dyrano</span>
      </div>
      <span class="brand-tagline">In-home personal training</span>
    </div>
  </section>

  <section class="card card-back">
    <div class="brand">
      <div class="brand-row">
        <span class="brand-dot"></span>
        <span class="brand-name">Dyrano</span>
      </div>
      <span class="brand-tagline">In-home personal training</span>
    </div>

    <div class="divider"></div>

    <div class="contact">
      <p class="person-name">Marta</p>
      <p class="person-role">Founder &amp; CEO</p>
      <ul class="contact-list">
        <li>
          <svg viewBox="0 0 16 16" aria-hidden="true"><path d="M4 2l2.5 3-1.5 1.5c.8 1.8 2.2 3.2 4 4L10.5 9l3 2.5-1.5 2.2C7 13.5 2.5 9 2.3 4z"/></svg>
          <span>306-555-0187</span>
        </li>
        <li>
          <svg viewBox="0 0 16 16" aria-hidden="true"><rect x="1.5" y="3.5" width="13" height="9"/><path d="M1.5 3.5L8 9l6.5-5.5"/></svg>
          <span>info@Dyrano.ca</span>
        </li>
        <li>
          <svg viewBox="0 0 16 16" aria-hidden="true"><circle cx="8" cy="8" r="6.5"/><ellipse cx="8" cy="8" rx="2.8" ry="6.5"/><path d="M1.5 8h13"/></svg>
          <span>www.Dyrano.ca</span>
        </li>
      </ul>
    </div>
  </section>
</main>
</body>
</html>
```